Company's Core Values to be on our Office Walls

We are a biotechnology consulting company in Massachusetts with about 40 employees. Please check out velmora.com for our look and more information on our business.

We have 4 core values in the company which we would like to display in our office. (Could be on our walls, could be placed in our website, could be placed anywhere. - We would like a multi-use for this graphic but PRIMARILY on our walls.)
No measurements involved yet, hence we'd like the source file to enable us to stretch the graphics. What's important is to see the designs in this contest.

Design: Looking for a wall display - decal, glass board, vinyl (we're open)
- of our Core Values to have in our reception. We want a Double-Helix
incorporated as the core values are "in our DNA" like the one attached
(would like to see some designs with the exact photo and some used as
inspiration for a unique creative design). Open to various sizes, we have a
few different walls we could place them on.

We are looking for a creative Core Value display to have in our new office. We want a sleek, out of the box design!

Velmora's 4 Core Values are:
> Put Others First
> Have the Courage to Take Action
> Take Personal Responsibility
> Have fun!
***We welcome any infographics per core value. We are open to your creativity!

**WE WANT THE ACTUAL CORE VALUES ON DISPLAY**
We already have a brand (attached).
Need our actual values on display in office.
We want the actual values on the wall, our logo can be incorporated but not
necessarily.

Overview of company: Young consulting firm for biotech and pharmaceuticals
in the Greater Boston area. We are service based, our employees are
engineers and specialists that work on our clients site. Company was
established in 2010, we moved into our New England office 3 months ago!

Colors: Our main color is blue but we also use orange, green, purple, and
teal. See velmora.com for our colors.

Target Market(s)

New Hires and Clients - We want to impress them!
Employees and clients - we want employees inspired by the core
values and clients to be impressed by them/separate us from the competition.

Industry/Entity Type

Biotechnology

Font styles to use
Sans Serif

Colors

Designer to choose colors to be used in the design.

Requirements
Must have
• Creativity!
• Some sort of tie to science/biotech
• Color - Blue is our company color but would like others as well. See website for brand colors.

```html
<!DOCTYPE html>
<html lang="en">
<head>
<meta charset="utf-8">
<title>Velmora Group – Core Values</title>
<link rel="stylesheet" href="https://fonts.googleapis.com/css2?family=Montserrat:wght@500;600;700&display=swap">
<style>
  :root {
    --backdrop: #d9d9d9;
    --navy-deep: #0b2748;
    --navy: #123d6c;
    --blue: #1d5c96;
    --helix-light: #8fc3e8;
    --helix-mid: #3f86bf;
    --glow: #5fe0f0;
    --green: #2aa04a;
    --green-light: #7ee08a;
    --purple: #3b2a6e;
    --purple-light: #7c68c0;
    --teal: #0e6f86;
    --teal-light: #4fcde0;
    --orange: #c97a10;
    --orange-light: #f5c04a;
    --white: #ffffff;
    --ink: #13304f;
  }
  * { box-sizing: border-box; margin: 0; padding: 0; }
  html, body { width: 1200px; height: 1200px; overflow: hidden; }
  body {
    background: var(--backdrop);
    font-family: "Montserrat", sans-serif;
    position: relative;
  }
  .poster {
    position: absolute;
    left: 276px; top: 98px;
    width: 654px; height: 1012px;
    overflow: hidden;
    background:
      radial-gradient(ellipse at 70% 30%, var(--blue) 0%, transparent 60%),
      linear-gradient(160deg, var(--navy) 0%, var(--navy-deep) 55%, var(--navy) 100%);
  }
  .helix-art {
    position: absolute;
    left: 144px; top: 0;
    width: 444px; height: 720px;
    background:
      linear-gradient(115deg, transparent 10%, rgba(143,195,232,0.55) 30%, rgba(63,134,191,0.35) 55%, rgba(143,195,232,0.45) 75%, transparent 92%);
    filter: blur(6px);
    opacity: 0.85;
  }
  .value {
    position: absolute;
    width: 176px; height: 176px;
    border-radius: 50%;
    transform: translate(-50%, -50%);
    border: 2px solid rgba(95,224,240,0.7);
    box-shadow: 0 0 28px rgba(95,224,240,0.55), inset 0 0 18px rgba(95,224,240,0.25);
    display: flex; align-items: center; justify-content: center;
  }
  .value__orb {
    width: 144px; height: 144px;
    border-radius: 50%;
    border: 4px solid rgba(255,255,255,0.75);
    display: flex; align-items: center; justify-content: center;
    text-align: center;
    color: var(--white);
    font-weight: 600;
    line-height: 1.05;
    text-shadow: 0 1px 3px rgba(0,0,0,0.45);
  }
  .value--others { left: 150px; top: 190px; }
  .value--others .value__orb { background: radial-gradient(circle at 50% 30%, var(--green-light), var(--green) 60%, #14592a); font-size: 25px; }
  .value--responsibility { left: 498px; top: 202px; }
  .value--responsibility .value__orb { background: radial-gradient(circle at 50% 30%, var(--purple-light), var(--purple) 60%, #1c1238); font-size: 15px; }
  .value--responsibility .value__text { display: block; transform: rotate(20deg); }
  .value--courage { left: 168px; top: 466px; }
  .value--courage .value__orb { background: radial-gradient(circle at 50% 30%, var(--teal-light), var(--teal) 60%, #06394a); font-size: 17px; }
  .value--fun { left: 534px; top: 550px; }
  .value--fun .value__orb { background: radial-gradient(circle at 50% 30%, var(--orange-light), var(--orange) 60%, #6e3f05); font-size: 29px; }
  .headline {
    position: absolute;
    left: 76px; top: 614px;
    color: var(--white);
    font-weight: 600;
    font-size: 117px;
    line-height: 96px;
    letter-spacing: -1px;
    text-shadow: 0 2px 12px rgba(0,0,0,0.35);
  }
  .corner {
    position: absolute;
    left: 0; top: 0;
    width: 654px; height: 1012px;
  }
  .brand {
    position: absolute;
    left: 384px; top: 846px;
    width: 240px;
    display: flex; flex-direction: column; align-items: center; gap: 16px;
    color: var(--ink);
    font-weight: 500;
    font-size: 22px;
    line-height: 1;
    letter-spacing: 2px;
    white-space: nowrap;
  }
  .brand__dot {
    width: 80px; height: 80px;
    border-radius: 50%;
    background: var(--ink);
  }
</style>
</head>
<body>
  <main class="poster">
    <div class="helix-art" role="img" aria-label="Glowing blue DNA double helix rising diagonally across a scientific data backdrop"></div>

    <div class="value value--others"><div class="value__orb">Put<br>Others<br>First</div></div>
    <div class="value value--responsibility"><div class="value__orb"><span class="value__text">Take<br>Personal<br>Responsibility</span></div></div>
    <div class="value value--courage"><div class="value__orb">Have the<br>Courage<br>to Take<br>Action</div></div>
    <div class="value value--fun"><div class="value__orb">Have<br>Fun!</div></div>

    <h1 class="headline">CORE<br>VALUES</h1>

    <svg class="corner" viewBox="0 0 654 1012" aria-hidden="true">
      <path d="M300 1012 C 390 900, 510 846, 654 822 L 654 1012 Z" fill="#ffffff"/>
    </svg>

    <div class="brand">
      <span class="brand__dot" aria-hidden="true"></span>
      <span class="brand__name">VELMORA GROUP</span>
    </div>
  </main>
</body>
</html>
```